Kestrel Vale is a new and completely innovative health supplement aimed at males between the ages of 25-60.

The supplement is formulated specifically to address two significant factors that affect men as they age. A reduction in the primary sex hormones and a reduction in their fertility.

I already have the logo design and label designed. I am looking to launch the product in January/February following successful trials.
The website won't need to have selling features inbuilt as I will be going through 3rd party platforms.

The website will however need to direct traffic to websites for a couple of purposes. In total I would expect to have in the region of 5-6 pages in total.

```html
<!DOCTYPE html>
<html lang="en">
<head>
<meta charset="utf-8">
<title>Kestrel Vale — Revive Your Vitality</title>
<link rel="stylesheet" href="https://fonts.googleapis.com/css2?family=Orbitron:wght@800;900&family=Roboto:wght@400;500;700&display=swap">
<style>
:root{
  --navy:#00072d;
  --blue:#00adef;
  --sky:#17c1f4;
  --light:#66d8fa;
  --mist:#f2fbfe;
  --stage:#efefef;
  --muted:#7a8391;
  --display:"Orbitron", sans-serif;
  --body:"Roboto", sans-serif;
}
*{margin:0;padding:0;box-sizing:border-box}
html,body{width:1200px;height:3011px;overflow:hidden}
body{background:var(--stage);font-family:var(--body);color:var(--navy);position:relative}
.page{position:absolute;left:203px;top:190px;width:794px;height:2630px;background:#fff}
.display{position:absolute;overflow:visible}
.display text{font-family:var(--display);font-weight:900}
.eyebrow{position:absolute;font-size:7px;letter-spacing:3.5px;color:var(--blue);text-transform:uppercase;white-space:nowrap}
.center{transform:translateX(-50%)}

/* hero */
.hero{position:absolute;left:10.5px;top:10.5px;width:774px;height:385px;background:var(--blue);border-radius:0 0 10px 10px;overflow:hidden}
.hero-portrait{position:absolute;left:586px;top:96px;width:189px;height:289px;background:radial-gradient(ellipse at 50% 40%,rgba(0,110,175,.45),rgba(0,173,239,0) 70%)}
.brand{position:absolute;display:flex;align-items:center;gap:5px;font-weight:700;color:#fff;white-space:nowrap}
.brand .dot{width:9px;height:9px;border-radius:50%;background:#fff}
.nav a{position:absolute;top:32px;font-size:7.5px;color:#fff;text-decoration:none}
.btn-inquiry{position:absolute;left:662px;top:14px;width:82px;height:27px;border-radius:14px;background:#fff;color:var(--navy);font-size:7px;font-weight:500;display:flex;align-items:center;justify-content:center}
.claim{position:absolute;top:209px;display:flex;align-items:center;gap:6px;color:#fff;font-size:7.2px;white-space:nowrap}
.claim svg{width:12px;height:12px}
.product-area{position:absolute;background:linear-gradient(180deg,#e6eef3,#f6f9fb);border-radius:8px}

/* stats */
.stat-label{position:absolute;top:601px;font-size:7.5px;color:var(--blue);white-space:nowrap;transform:translateX(-50%)}

/* about */
.copy{position:absolute;font-size:7.4px;line-height:12px;color:var(--muted)}
.check{position:absolute;display:flex;align-items:center;gap:5px;font-size:7.4px;color:var(--muted);white-space:nowrap}
.check i{width:8px;height:8px;border:1px solid var(--blue);border-radius:50%}
.photo{position:absolute;border-radius:4px}
.photo.about-man{left:405px;top:666px;width:283px;height:282px;background:linear-gradient(160deg,#a9b1bb,#7e8a98 55%,#4f7fb5)}

/* features */
.panel{position:absolute;left:10.5px;width:774px;background:var(--mist)}
.feature{position:absolute;display:flex;align-items:center;gap:10px;font-size:11px;line-height:12px;color:var(--navy);white-space:nowrap}
.feature.right{flex-direction:row-reverse;text-align:right}
.ic{width:42px;height:42px;flex:none;display:flex;align-items:center;justify-content:center}
.ic.round{border-radius:50%;background:#fff;box-shadow:0 2px 8px rgba(0,173,239,.12)}

/* ingredients */
.tab{position:absolute;top:1533px;width:103px;height:28px;border-radius:14px;background:var(--mist);font-size:7px;display:flex;align-items:center;justify-content:center;color:var(--navy)}
.tab.active{background:#cdeffb}
.th{position:absolute;top:1598px;font-size:9.5px;color:var(--navy)}
.td{position:absolute;font-size:7.5px;color:var(--muted)}
.td.mg{color:var(--blue);text-align:right;width:60px}
.capsule-art{position:absolute;left:338px;top:1627px;width:122px;height:132px;background:radial-gradient(ellipse at 50% 40%,rgba(102,216,250,.35),rgba(242,251,254,0) 70%)}

/* faq */
.photo.faq-man{left:114px;top:1891px;width:248px;height:278px;background:linear-gradient(170deg,#c9ced4,#9aa3ad 50%,#4f7fb5)}
.faq-item{position:absolute;left:405px;width:282px;background:#fff;border-radius:3px;box-shadow:0 2px 8px rgba(0,7,45,.05);font-size:7px;color:var(--navy)}
.faq-item .q{position:absolute;left:16px;top:50%;transform:translateY(-50%);white-space:nowrap}
.faq-item .toggle{position:absolute;right:12px;top:50%;transform:translateY(-50%);width:14px;height:14px;border-radius:3px;display:flex;align-items:center;justify-content:center;font-size:9px;color:var(--navy);background:#f4f6f8}
.faq-item.open .q{top:16px;transform:none}
.faq-item.open .toggle{top:12px;transform:none;background:var(--blue);color:#fff}
.faq-item .a{position:absolute;left:16px;top:38px;width:255px;font-size:6.8px;line-height:11.5px;color:var(--muted)}

/* subscribe */
.subscribe-field{position:absolute;left:250px;top:2355px;width:259px;height:41px;background:#fff;box-shadow:0 4px 14px rgba(0,7,45,.06);font-size:7px;color:var(--muted);display:flex;align-items:center;padding-left:14px;z-index:1}
.subscribe-btn{position:absolute;left:509px;top:2355px;width:41px;height:41px;background:var(--blue);display:flex;align-items:center;justify-content:center;z-index:1}
.product-faded{position:absolute;left:311px;top:2397px;width:152px;height:60px;background:linear-gradient(180deg,#eef2f5,#ffffff)}

/* footer */
.footer{position:absolute;left:10.5px;top:2460px;width:774px;height:160px;background:var(--blue);border-radius:10px}
.footer-link{position:absolute;top:2536px;font-size:7.4px;color:#fff;text-decoration:none}
.copyright{position:absolute;top:2555px;left:397px;transform:translateX(-50%);font-size:6.4px;color:#fff;white-space:nowrap}
.social{position:absolute;top:2534px;left:506px;display:flex;align-items:center;gap:10px;font-size:7.4px;color:#fff;white-space:nowrap}
.social i{width:9px;height:9px;border-radius:50%;background:#fff;display:block}
</style>
</head>
<body>
<main class="page">

  <!-- Hero -->
  <section class="hero">
    <div class="hero-portrait" role="img" aria-label="Smiling man in soft blue tint, blended into the hero background"></div>
  </section>
  <div class="brand" style="left:28px;top:30px;font-size:11px"><span class="dot"></span>Kestrel Vale</div>
  <nav class="nav">
    <a style="left:224px">About</a>
    <a style="left:305px">Features</a>
    <a style="left:392px">Ingredients</a>
    <a style="left:478px">FAQS</a>
    <a style="left:554px">Contact</a>
  </nav>
  <div class="btn-inquiry">Make an Inquiry</div>

  <svg class="display" style="left:0;top:0" width="794" height="220">
    <text x="397" y="138" text-anchor="middle" font-size="34" fill="#fff" textLength="354" lengthAdjust="spacingAndGlyphs">REVIVE YOUR</text>
    <text x="397" y="186" text-anchor="middle" font-size="54" fill="var(--navy)" textLength="354" lengthAdjust="spacingAndGlyphs">VITALITY</text>
  </svg>

  <div class="claim" style="left:219px">
    <svg viewBox="0 0 12 12"><circle cx="6" cy="6" r="5.3" fill="none" stroke="#fff" stroke-width=".9"/><path d="M3.6 6.1l1.7 1.7 3.2-3.4" fill="none" stroke="#fff" stroke-width=".9"/></svg>
    Supports and Optimizes Testosterone Levels
  </div>
  <div class="claim" style="left:422px">
    <svg viewBox="0 0 12 12"><circle cx="6" cy="6" r="5.3" fill="none" stroke="#fff" stroke-width=".9"/><path d="M3.6 6.1l1.7 1.7 3.2-3.4" fill="none" stroke="#fff" stroke-width=".9"/></svg>
    Optimizes Fertility and Sperm Production
  </div>

  <div class="product-area" role="img" aria-label="Product photo: three supplement bottles with capsules" style="left:276px;top:248px;width:245px;height:270px"></div>

  <!-- Stats -->
  <svg class="display" style="left:0;top:560px" width="794" height="40">
    <text x="145" y="36" text-anchor="middle" font-size="31" fill="var(--navy)">180</text>
    <text x="305" y="36" text-anchor="middle" font-size="31" fill="var(--navy)">62</text>
    <text x="486" y="36" text-anchor="middle" font-size="31" fill="var(--navy)">4</text>
    <text x="646" y="36" text-anchor="middle" font-size="31" fill="var(--navy)">357</text>
  </svg>
  <div class="stat-label" style="left:145px">Capsules</div>
  <div class="stat-label" style="left:305px">Per MG</div>
  <div class="stat-label" style="left:486px">Combined Ingredients</div>
  <div class="stat-label" style="left:646px">Tests Taken Before Launch</div>

  <!-- About -->
  <div class="eyebrow" style="left:107px;top:672px">About</div>
  <svg class="display" style="left:107px;top:680px" width="220" height="64">
    <text x="0" y="28" font-size="28" fill="var(--navy)" textLength="198" lengthAdjust="spacingAndGlyphs">KESTREL</text>
    <text x="0" y="58" font-size="28" fill="var(--navy)" textLength="136" lengthAdjust="spacingAndGlyphs">VALE</text>
  </svg>
  <p class="copy" style="left:107px;top:762px;width:250px">Kestrel Vale is formulated with a blend of natural ingredients known for their ability to support healthy testosterone levels. Whether you're an athlete looking to enhance performance or someone seeking to reclaim youthful vigor, Kestrel Vale is here for you.</p>
  <div class="check" style="left:107px;top:824px"><i></i>Dummy Text Fille Here</div>
  <div class="check" style="left:217px;top:824px"><i></i>Dummy Text Filler Goes Here</div>
  <div class="check" style="left:107px;top:843px"><i></i>Dummy Text Fille Here</div>
  <div class="check" style="left:217px;top:843px"><i></i>Dummy Text Filler Goes Here</div>
  <p class="copy" style="left:107px;top:866px;width:250px">For those on the path to fatherhood or simply aiming to maintain reproductive wellness, our product is tailored to meet your needs.</p>
  <div class="photo about-man" role="img" aria-label="Smiling man in a denim shirt holding a supplement bottle and giving a thumbs up"></div>

  <!-- Features -->
  <section class="panel" style="top:1003px;height:374px"></section>
  <div class="eyebrow center" style="left:397px;top:1051px">Formula</div>
  <svg class="display" style="left:0;top:1060px" width="794" height="36">
    <text x="397" y="30" text-anchor="middle" font-size="30" fill="var(--navy)" textLength="228" lengthAdjust="spacingAndGlyphs">FEATURES</text>
  </svg>

  <div class="feature" style="left:130px;top:1138px">
    <span class="ic round"><svg width="18" height="18" viewBox="0 0 18 18" fill="none" stroke="var(--blue)" stroke-width="1"><rect x="5" y="3" width="8" height="13" rx="1.5"/><path d="M7.5 1.5h3M9.8 6.5L8 9.5h2.2L8.4 12.5"/></svg></span>
    <span>Increased<br>Energy</span>
  </div>
  <div class="feature" style="left:105px;top:1211px">
    <span class="ic"><svg width="42" height="46" viewBox="0 0 42 46"><path d="M21 1l19 11v22L21 45 2 34V12z" fill="var(--blue)"/><path d="M14 30c0-9 6-14 15-15-1 9-6 15-15 15zm0 0l8-8" fill="none" stroke="#fff" stroke-width="1.1"/></svg></span>
    <span>Natural<br>Ingredients</span>
  </div>
  <div class="feature" style="left:130px;top:1283px">
    <span class="ic round"><svg width="20" height="20" viewBox="0 0 20 20" fill="none" stroke="var(--blue)" stroke-width="1"><circle cx="7" cy="7" r="3"/><circle cx="13" cy="7" r="3"/><path d="M10 10v3M7 14l1 1M13 14l-1 1M10 17v1"/></svg></span>
    <span>Bio<br>Formula</span>
  </div>

  <div class="feature right" style="right:126px;top:1136px">
    <span class="ic"><svg width="42" height="46" viewBox="0 0 42 46"><path d="M21 1l19 11v22L21 45 2 34V12z" fill="var(--blue)"/><circle cx="21" cy="23" r="8" fill="none" stroke="#fff" stroke-width="1.1"/><circle cx="21" cy="23" r="3.5" fill="none" stroke="#fff" stroke-width="1.1"/></svg></span>
    <span>Reduce<br>Fertility</span>
  </div>
  <div class="feature right" style="right:105px;top:1211px">
    <span class="ic round"><svg width="22" height="14" viewBox="0 0 22 14" fill="none" stroke="var(--blue)" stroke-width=".9"><path d="M2 10l3-2 3 2v3l-3 1-3-1zM8 10l3-2 3 2v3M14 10l3-2 3 2M17 8V4l3-2"/></svg></span>
    <span>Optimize Testosterone<br>Level</span>
  </div>
  <div class="feature right" style="right:126px;top:1281px">
    <span class="ic"><svg width="42" height="46" viewBox="0 0 42 46"><path d="M21 1l19 11v22L21 45 2 34V12z" fill="var(--blue)"/><ellipse cx="26" cy="18" rx="4" ry="3" fill="none" stroke="#fff" stroke-width="1.1" transform="rotate(-35 26 18)"/><path d="M23 21c-3 3-1 5-5 7s-3 3-5 4" fill="none" stroke="#fff" stroke-width="1.1"/></svg></span>
    <span>Optimize<br>Sperm Production</span>
  </div>

  <div class="product-area" role="img" aria-label="Product photo: tilted supplement bottle" style="left:322px;top:1130px;width:160px;height:265px"></div>

  <!-- Ingredients -->
  <div class="eyebrow center" style="left:397px;top:1465px">Supplement Facts</div>
  <svg class="display" style="left:0;top:1474px" width="794" height="36">
    <text x="397" y="30" text-anchor="middle" font-size="30" fill="var(--navy)" textLength="272" lengthAdjust="spacingAndGlyphs">INGREDIENTS</text>
  </svg>
  <div class="tab" style="left:107px">Text Filler</div>
  <div class="tab" style="left:226px">Text Filler</div>
  <div class="tab active" style="left:345px">Vitamin B6</div>
  <div class="tab" style="left:464px">Text Filler</div>
  <div class="tab" style="left:583px">Text Filler</div>

  <div class="th" style="left:224px">Ingredients</div>
  <div class="th" style="left:495px">Per Serving (MG)</div>
  <div class="capsule-art" role="img" aria-label="Open capsule spilling powder"></div>
  <div class="td" style="left:225px;top:1633px">Text Filler</div>
  <div class="td" style="left:225px;top:1657px">Text Filler</div>
  <div class="td" style="left:225px;top:1681px">Text Filler</div>
  <div class="td" style="left:225px;top:1705px">Text Filler</div>
  <div class="td" style="left:225px;top:1729px">Text Filler</div>
  <div class="td mg" style="left:510px;top:1633px">20mg</div>
  <div class="td mg" style="left:510px;top:1657px">20mg</div>
  <div class="td mg" style="left:510px;top:1681px">20mg</div>
  <div class="td mg" style="left:510px;top:1705px">20mg</div>
  <div class="td mg" style="left:510px;top:1729px">20mg</div>

  <!-- FAQ -->
  <section class="panel" style="top:1792px;height:428px"></section>
  <div class="photo faq-man" role="img" aria-label="Smiling man in a denim shirt holding a bottle and capsules in his hands"></div>
  <div class="eyebrow" style="left:405px;top:1876px">FAQS</div>
  <svg class="display" style="left:405px;top:1884px" width="300" height="62">
    <text x="0" y="28" font-size="28" fill="var(--navy)" textLength="282" lengthAdjust="spacingAndGlyphs">FREQUENTLY</text>
    <text x="0" y="57" font-size="28" fill="var(--navy)" textLength="146" lengthAdjust="spacingAndGlyphs">ASKED</text>
  </svg>
  <div class="faq-item" style="top:1968px;height:33px"><span class="q">How Much Does it Cost?</span><span class="toggle">+</span></div>
  <div class="faq-item open" style="top:2008px;height:79px">
    <span class="q">What are the ingredients of Kestrel Vale?</span><span class="toggle">&minus;</span>
    <p class="a">Lorem ipsum dolor sit amet, consectetur adipiscing elit, sed do eiusmo tempor incididunt ut labore et dolore magna aliqua. Quis ipsum suspendisse ultrices gravida. Risus commodo viverra maecenas accumsan lacus vel facilisis.</p>
  </div>
  <div class="faq-item" style="top:2094px;height:33px"><span class="q">How Kestrel Vale Helps?</span><span class="toggle">+</span></div>
  <div class="faq-item" style="top:2135px;height:33px"><span class="q">What are the ingredients of Kestrel Vale?</span><span class="toggle">+</span></div>

  <!-- Subscribe -->
  <div class="eyebrow center" style="left:397px;top:2274px">Get Notified About Its Launch</div>
  <svg class="display" style="left:0;top:2283px" width="794" height="36">
    <text x="397" y="30" text-anchor="middle" font-size="30" fill="var(--navy)" textLength="249" lengthAdjust="spacingAndGlyphs">SUBSCRIBE</text>
  </svg>
  <div class="product-faded" role="img" aria-label="Faded product photo behind the form"></div>
  <div class="subscribe-field">Enter Your Email Address and Join the Waiting Line...</div>
  <div class="subscribe-btn"><svg width="14" height="14" viewBox="0 0 14 14"><path d="M1 6.5L13 1 9 13 6.5 8z" fill="#fff"/><path d="M6.5 8L13 1" stroke="var(--blue)" stroke-width=".8"/></svg></div>

  <!-- Footer -->
  <footer class="footer"></footer>
  <a class="footer-link" style="left:107px">Features</a>
  <a class="footer-link" style="left:179px">Ingredients</a>
  <a class="footer-link" style="left:260px">Contact</a>
  <div class="brand" style="left:397px;top:2530px;font-size:10px;transform:translateX(-50%)"><span class="dot"></span>Kestrel Vale</div>
  <div class="copyright">© 2025 Kestrel Vale - All Right Reserved</div>
  <div class="social">Follow Our Social Media:<i></i><i></i><i></i><i></i><i></i></div>

</main>
</body>
</html>
```